New Word Template Design Project

I want design about template plant LUMEN COVE tree
The size is A4/Users/mibu/Desktop/DSC07540.JPG
/Users/mibu/Desktop/DSC07514.JPG

```html
<!DOCTYPE html>
<html lang="en">
<head>
<meta charset="utf-8">
<title>Lumen Cove Stationery</title>
<link href="https://fonts.googleapis.com/css2?family=Montserrat:wght@400;500&family=Open+Sans:wght@400;600&family=Roboto:wght@300;400&display=swap" rel="stylesheet">
<style>
  :root {
    --backdrop: #3b3f42;
    --paper: #ffffff;
    --teal: #0b8a7c;
    --teal-bright: #17a79a;
    --mint: #c8f5ee;
    --mint-deep: #9fe6da;
    --ink-soft: #8a8f93;
    --ink-faint: #a4a9ad;
  }
  * { margin: 0; padding: 0; box-sizing: border-box; }
  html, body { width: 1200px; height: 1200px; overflow: hidden; }
  body {
    background: var(--backdrop);
    position: relative;
    font-family: "Roboto", Arial, sans-serif;
  }
  .piece { position: absolute; overflow: hidden; }

  /* Brand lockup */
  .brand-dot { position: absolute; border-radius: 50%; background: var(--teal-bright); }
  .brand-name {
    position: absolute;
    font-family: "Montserrat", Arial, sans-serif;
    font-weight: 500;
    color: var(--teal);
    letter-spacing: 0.12em;
    white-space: nowrap;
    transform: translateX(-50%);
  }

  /* Letterhead */
  .letterhead { left: 112px; top: 108px; width: 451px; height: 647px; background: var(--paper); }
  .letterhead .watermark {
    position: absolute; left: 254px; top: 398px; width: 254px; height: 254px;
    border-radius: 50%;
    background: radial-gradient(circle, #eefaf8 0%, #e2f5f2 70%, #d8f1ed 100%);
    opacity: 0.8;
  }
  .letterhead .dateline { position: absolute; right: 44px; top: 110px; font-size: 9.5px; color: var(--teal-bright); }
  .letterhead .sender { position: absolute; right: 44px; top: 129px; font-size: 9.5px; line-height: 13.5px; color: var(--ink-soft); text-align: right; font-weight: 300; }
  .letterhead .body-copy { position: absolute; left: 50px; width: 359px; font-size: 8.9px; line-height: 13.4px; color: var(--ink-soft); text-align: justify; font-weight: 300; }
  .letterhead .contact-title { position: absolute; left: 50px; top: 561px; font-size: 8px; color: var(--teal-bright); }
  .letterhead .contact-col { position: absolute; top: 578px; font-size: 6.2px; line-height: 10.5px; color: var(--ink-faint); }
  .letterhead .footer-rule { position: absolute; left: 50px; top: 604px; width: 366px; height: 1px; background: var(--teal-bright); }

  /* Notebook */
  .notebook { left: 642px; top: 101px; width: 452px; height: 654px; }
  .notebook .cover-art { position: absolute; inset: 0; background: linear-gradient(180deg, #c4f3ec 0%, #b6ece4 55%, #c9f5ef 100%); }
  .notebook .elastic-band { position: absolute; left: 393px; top: 7px; width: 17px; height: 647px; background: var(--teal); }

  /* Business card front */
  .card-front { left: 112px; top: 830px; width: 451px; height: 258px; }
  .card-front .card-art { position: absolute; inset: 0; background: linear-gradient(135deg, #2cc7b4 0%, #86e3d7 50%, #25b8a6 100%); }

  /* Business card back */
  .card-back { left: 642px; top: 830px; width: 452px; height: 258px; background: var(--paper); }
  .card-back .info-panel { position: absolute; left: 227px; top: 0; width: 225px; height: 258px; background: var(--teal); color: #ffffff; font-family: "Open Sans", Arial, sans-serif; }
  .card-back .person-name { position: absolute; left: 43px; top: 64px; font-size: 25px; font-weight: 600; }
  .card-back .person-role { position: absolute; left: 43px; top: 98px; font-size: 12px; }
  .card-back .contact-row { position: absolute; left: 43px; font-size: 11px; display: flex; align-items: center; gap: 9px; }
  .card-back .contact-row svg { width: 11px; height: 11px; fill: #ffffff; }
</style>
</head>
<body>

<section class="piece letterhead">
  <div class="watermark" role="img" aria-label="Faint circular brand decoration"></div>
  <div class="brand-dot" style="left:45px;top:48px;width:56px;height:56px;"></div>
  <div class="brand-name" style="left:73px;top:111px;font-size:10px;">LUMEN COVE</div>

  <div class="dateline">November 1, 2020</div>
  <div class="sender">your company name<br>T (123) 455 7899</div>

  <p class="body-copy" style="top:171px;">Dear Mr. Aldren,</p>
  <p class="body-copy" style="top:201px;">Us sum verovidunt vent lit laccum vel in rescilis nim fugia dia inus am at aut pratis eius, consectent.Pient plia voluptatem quiaspel incipsa ecatiusam, quaepro commo endiatum lauda simusda simus accatem quatate voluptur sequae nullitium aruntis maximil lorpos solore.</p>
  <p class="body-copy" style="top:267px;">sequaest, te perupicto exero ius verion con restium es nonsequi tempeli taquam alitatibus ipidunt, quatesciae et explaborem am rem eumquo consequis alique et re perum sum is sa niendigenit vendescime necte pedit abo.</p>
  <p class="body-copy" style="top:320px;">Quidebit possim accabor eroress imporum quid quam sit moluptatur seris sus id et, quunt aci ut lam eaque vent officipisqui blatin repudae perat.Rum non num lam idisseque la nusciis alitiaectum dolent plabor reribuscim inullique modi nim eiureic itisquaest quam corem dem invelen ihiliqu aeperitatus eum. Eturem rerum voluptiis aut estiat mos et exeritconemol orruptiorios sequi ratusci undictati tem ium cor ra nectatendi omnihil labora nossit quam volor milloribus maionse sum dellibu sanietu reperisitat omnis dolestisque occusam ilitatur? Quidebit autet facerae conse etur, con est vel et ea dolectum dellibus.</p>
  <p class="body-copy" style="top:456px;">Sincerely yours,</p>
  <p class="body-copy" style="top:483px;">Your name<br>Managing Director</p>

  <div class="contact-title">Contact Details</div>
  <div class="contact-col" style="left:50px;">your company name<br>T (123) 455 7899</div>
  <div class="contact-col" style="left:186px;">Your address sample. Your address<br>sample. Your address sample.</div>
  <div class="contact-col" style="left:341px;">info@yourcompany.com<br>www.yourcompany.com</div>
  <div class="footer-rule"></div>
</section>

<section class="piece notebook">
  <div class="cover-art" role="img" aria-label="Large pale palm tree illustration covering the notebook"></div>
  <div class="brand-dot" style="left:166px;top:142px;width:116px;height:116px;"></div>
  <div class="brand-name" style="left:224px;top:274px;font-size:19px;">LUMEN COVE</div>
  <div class="elastic-band"></div>
</section>

<section class="piece card-front">
  <div class="card-art" role="img" aria-label="Palm fronds illustration in mint and teal"></div>
  <div class="brand-dot" style="left:200px;top:103px;width:58px;height:58px;"></div>
  <div class="brand-name" style="left:229px;top:166px;font-size:9.5px;">LUMEN COVE</div>
</section>

<section class="piece card-back">
  <div class="brand-dot" style="left:77px;top:73px;width:72px;height:72px;"></div>
  <div class="brand-name" style="left:113px;top:154px;font-size:9.5px;">LUMEN COVE</div>
  <div class="info-panel">
    <div class="person-name">Rana Vale</div>
    <div class="person-role">MANAGING DIRECTOR</div>
    <div class="contact-row" style="top:150px;">
      <svg viewBox="0 0 24 24"><path d="M6.6 10.8a15.1 15.1 0 0 0 6.6 6.6l2.2-2.2a1 1 0 0 1 1-.25 11.4 11.4 0 0 0 3.6.57 1 1 0 0 1 1 1V20a1 1 0 0 1-1 1A17 17 0 0 1 3 4a1 1 0 0 1 1-1h3.5a1 1 0 0 1 1 1c0 1.25.2 2.45.57 3.57a1 1 0 0 1-.25 1z"/></svg>
      <span>(+00)123.456.780</span>
    </div>
    <div class="contact-row" style="top:169px;">
      <svg viewBox="0 0 24 24"><path d="M2 5h20v14H2z M2 5l10 8 10-8" fill="none" stroke="#fff" stroke-width="2"/></svg>
      <span>mail@example.com</span>
    </div>
    <div class="contact-row" style="top:188px;">
      <svg viewBox="0 0 24 24"><g fill="none" stroke="#fff" stroke-width="2"><circle cx="12" cy="12" r="10"/><path d="M2 12h20M12 2c3 3 3 17 0 20M12 2c-3 3-3 17 0 20"/></g></svg>
      <span>www.example.com</span>
    </div>
  </div>
</section>

</body>
</html>
```